KRWM new business card design

We need a business card design for our established business which is Australia wide however based in Melbourne. We are a young team of Financial Planners who specialize in Insurance and Basic super advice for people like us.

We are people who help our clients get things done in a timely and cost effective manner whilst having a good time and a laugh along the way.

We would like this to have a consistent feel with our new e-brochure which i have attached from a color and font perspective.

Industry/Entity Type

Business

Requirements
Must have
• We do not need specific address details rather just the states we are in:

VIC/NSW/QLD/TAS
Nice to have
• Curved edge to mate the brochure

```html
<!DOCTYPE html>
<html lang="en">
<head>
<meta charset="utf-8">
<title>KRWM business card set</title>
<link href="https://fonts.googleapis.com/css2?family=Arimo:ital,wght@0,400;0,700;1,700&family=PT+Sans&display=swap" rel="stylesheet">
<style>
:root{
  --green:#6cbd45;
  --green-deep:#1fa04a;
  --ink:#111;
  --grey:#6b6b6b;
  --dark-grey:#3a3a3a;
  --white:#fff;
  --stage:#ece8e2;
}
*{margin:0;padding:0;box-sizing:border-box}
html,body{width:1200px;height:788px;overflow:hidden;background:var(--stage)}
.canvas{position:relative;width:1200px;height:788px;font-family:"Arimo",Arial,sans-serif}
.label{position:absolute;width:525px;text-align:center;font-family:"PT Sans",sans-serif;font-size:23px;color:#222}
.card{position:absolute;width:525px;height:300px;border-radius:18px;overflow:hidden;box-shadow:0 3px 10px rgba(0,0,0,.25)}
.card--front{left:53px;top:72px;background:radial-gradient(circle at 40% 35%,#3b3b3b 0%,#141414 55%,#050505 100%)}
.card--back1{left:622px;top:75px;height:298px;background:var(--white)}
.card--back2{left:53px;top:445px;background:var(--white)}
.card--back3{left:622px;top:445px;background:radial-gradient(circle at 35% 45%,#3a3a3a 0%,#1c1c1c 60%,#0d0d0d 100%)}
.brand{position:absolute;display:flex;align-items:center;gap:10px;font-weight:700;font-size:46px;letter-spacing:1px}
.brand__square{width:22px;height:22px;background:var(--green)}
.brand--light{color:var(--white)}
.brand--dark{color:var(--ink)}
.divider{position:absolute;width:2px;background:linear-gradient(to bottom,transparent,#777 50%,transparent)}
.contact{position:absolute;left:317px;top:76px;list-style:none;color:var(--white);font-size:14px;line-height:26px}
.contact b{font-weight:700;font-style:italic}
.band{position:absolute;left:0;right:0;bottom:0;height:38px;background:var(--green);color:var(--white);font-weight:700;display:flex;align-items:center}
.band--name{padding-left:57px;font-size:15px}
.band--name small{font-size:13px}
.band--tagline{justify-content:center;font-size:14px}
.services{position:absolute;list-style:none;font-weight:700;font-size:14px}
.services__title{font-style:italic;font-size:18px;margin-bottom:12px}
.services li{line-height:34px}
.services li::before{content:"▪ "}
.services--grey{left:320px;top:44px;color:var(--grey)}
.services--grey .services__title{color:var(--grey);margin-bottom:4px}
.services--centre{left:0;right:0;top:44px;text-align:center;color:var(--dark-grey)}
.services--centre .services__title{margin-bottom:4px}
.services--light{left:313px;top:23px;color:var(--white)}
.services--light .services__title{margin-bottom:2px}
.tagline{position:absolute;font-weight:700;font-size:14px}
.tagline--bottom{left:0;right:0;top:268px;text-align:center;color:var(--dark-grey)}
.tagline--green{left:313px;top:252px;color:var(--green);line-height:18px}
</style>
</head>
<body>
<div class="canvas">
  <p class="label" style="left:53px;top:33px">Front</p>
  <p class="label" style="left:622px;top:33px">Back - 1</p>
  <p class="label" style="left:53px;top:403px">Back - 2</p>
  <p class="label" style="left:622px;top:403px">Back - 3</p>

  <section class="card card--front">
    <div class="brand brand--light" style="left:62px;top:110px"><span class="brand__square"></span>KRWM</div>
    <div class="divider" style="left:262px;top:58px;height:180px"></div>
    <ul class="contact">
      <li><b>cell</b> 0400 555 217</li>
      <li><b>phone</b> 1300 555 418</li>
      <li><b>fax</b> 03 9555 0174</li>
      <li><b>email</b> daniel@krwm.com.au</li>
      <li><b>web</b> www.krwm.com.au</li>
      <li>VIC/NSW/QLD/TAS</li>
    </ul>
    <div class="band band--name">Daniel Harrow -&nbsp;<small>ADFS, BBus, LRS©, Financial Adviser</small></div>
  </section>

  <section class="card card--back1">
    <div class="brand brand--dark" style="left:68px;top:110px"><span class="brand__square"></span>KRWM</div>
    <div class="divider" style="left:261px;top:20px;height:235px"></div>
    <ul class="services services--grey">
      <li class="services__title" style="list-style:none">Specialising in</li>
      <li>Risk Insurance</li>
      <li>Debt Management</li>
      <li>Superannuation</li>
      <li>Wealth Creation</li>
      <li>Retirement Planning</li>
    </ul>
    <div class="band band--tagline">SECURE FUTURE, ENHANCED LIFESTYLE</div>
  </section>

  <section class="card card--back2">
    <ul class="services services--centre">
      <li class="services__title">Specialising in</li>
      <li>Risk Insurance</li>
      <li>Debt Management</li>
      <li>Superannuation</li>
      <li>Wealth Creation</li>
      <li>Retirement Planning</li>
    </ul>
    <p class="tagline tagline--bottom">SECURE FUTURE, ENHANCED LIFESTYLE</p>
  </section>

  <section class="card card--back3">
    <div class="brand brand--light" style="left:50px;top:120px;font-size:52px"><span class="brand__square"></span>KRWM</div>
    <ul class="services services--light">
      <li class="services__title">Specialising in</li>
      <li>Risk Insurance</li>
      <li>Debt Management</li>
      <li>Superannuation</li>
      <li>Wealth Creation</li>
      <li>Retirement Planning</li>
    </ul>
    <p class="tagline tagline--green">SECURE FUTURE<br>ENHANCED LIFESTYLE</p>
  </section>
</div>
</body>
</html>
```